Create a Brochure Design for Thornbury Homecare

Thornbury Homecare is a subsidiary of the Thornbury Care Group. This brochure is specifically for the Thornbury Homecare company and brand. Create a 3 panel, A4, front and back, tri-fold brochure. This brochure will be a way to introduce our Homecare services to the community, prospective clients, and various referral partners. The brochure must be eye catching, unique in its deliverables and demonstrate both attention to detail and comfort. Our organization is sophisticated and built around warmth, care and individualized personal attention. The most important aspect of this design is to focus on creating a nurturing, warm, and inviting feel where you would want to have a Nurse or Nurse’s Aide in your own home or a loved one’s home.

I am open to the creativity of the designer to develop something based on the above criteria; however I would like the design to work well with the existing collateral material. What I mean by that is that while I want everything to have its own personality and stand out as its own brand representative, I still need to be able to tell that the overall design concept stays stylistically inside of the same ‘family’ of existing designed material. Because of this, below I would like for the designer to pull inspiration from the link to our website (Located below) as well as from the attachment of our recently refreshed business cards (Attached). This should allow each design to be unique and creative, while still staying inside of a framework and the feel/style that I am looking for.

Finally, I want all the designers to understand that this brochure design is for a private, in home, healthcare company where we are responsible for providing personalized care for a culturally and ethnically diverse make-up clientele of all ages. The photos that are used must represent an image of warmth, care, and a positive interaction between client and caregiver.

Look under the Thornbury Homecare tab at www.thornburycaregroup-example.net
Updates

Industry/Entity Type

Healthcare

Requirements
Must have
• • The Thornbury Homecare company logo must be included.

```html
<!DOCTYPE html>
<html lang="en">
<head>
<meta charset="utf-8">
<title>Thornbury Homecare – Tri-fold Brochure</title>
<link rel="stylesheet" href="https://fonts.googleapis.com/css2?family=Arimo:ital,wght@0,400;0,700;1,400&family=Roboto+Condensed:ital,wght@1,700&family=Libre+Baskerville:ital@1&display=swap">
<style>
  :root {
    --lime: #c3d957;
    --lime-soft: #e3edb0;
    --leaf: #8cc63f;
    --forest: #1f7a3a;
    --forest-deep: #17612d;
    --salmon: #e8876a;
    --salmon-soft: #f2b59f;
    --brand: #2f6f50;
    --paper: #ffffff;
    --stage: #f4f4f2;
    --ink: #2b2b2b;
  }
  * { box-sizing: border-box; margin: 0; padding: 0; }
  html, body { width: 1200px; height: 750px; overflow: hidden; background: var(--stage); }
  .canvas { position: relative; width: 1200px; height: 750px; }
  .brochure {
    position: absolute; left: 120px; top: 36px; width: 960px; height: 679px;
    background: var(--paper); box-shadow: 0 6px 24px rgba(0,0,0,.12); overflow: hidden;
  }
  .brochure-art { position: absolute; inset: 0; }
  .panel { position: absolute; top: 0; width: 320px; height: 679px; }
  .panel--promise { left: 0; }
  .panel--contact { left: 320px; }
  .panel--cover { left: 640px; }

  .promise-title {
    position: absolute; left: 150px; top: 14px; white-space: nowrap;
    font-family: "Roboto Condensed", Arial, sans-serif; font-style: italic; font-weight: 700;
    color: var(--paper); line-height: 1.02; text-transform: uppercase;
  }
  .promise-title .lead { display: block; font-size: 16px; }
  .promise-title .main { display: block; font-size: 36px; color: var(--forest); margin-top: 2px; }

  .promise-copy {
    position: absolute; left: 34px; top: 300px; width: 260px;
    font-family: "Arimo", Arial, sans-serif; font-size: 12px; line-height: 1.38;
    color: var(--ink); text-align: center;
  }
  .promise-copy p + p { margin-top: 8px; }
  .promise-copy strong { font-weight: 700; }

  .contact-block {
    position: absolute; left: 30px; top: 560px; width: 260px; font-style: normal;
    font-family: "Arimo", Arial, sans-serif; color: var(--paper); text-align: center;
  }
  .contact-name { font-weight: 700; font-size: 15px; letter-spacing: .03em; text-transform: uppercase; margin-bottom: 6px; }
  .contact-line { font-size: 10.5px; line-height: 1.45; }

  .brand-lockup {
    position: absolute; left: 96px; top: 446px; display: flex; align-items: center; gap: 8px;
    white-space: nowrap;
  }
  .brand-mark { width: 14px; height: 14px; background: var(--salmon); flex: none; }
  .brand-name {
    font-family: "Arimo", Arial, sans-serif; font-weight: 700; font-size: 18px; color: var(--brand);
  }
  .brand-tagline {
    position: absolute; left: 118px; top: 476px; width: 190px;
    font-family: "Libre Baskerville", Georgia, serif; font-style: italic; font-size: 10px;
    line-height: 1.5; color: var(--brand);
  }
</style>
</head>
<body>
<div class="canvas">
  <div class="brochure">
    <svg class="brochure-art" viewBox="0 0 960 679" width="960" height="679">
      <defs>
        <linearGradient id="promise-bg" x1="0" y1="0" x2="0" y2="1">
          <stop offset="0" stop-color="#ffffff"/>
          <stop offset=".42" stop-color="#f1f6e2"/>
          <stop offset=".72" stop-color="#9ccd5a"/>
          <stop offset="1" stop-color="#2f8a38"/>
        </linearGradient>
        <linearGradient id="bokeh-bg" x1="0" y1="0" x2="0" y2="1">
          <stop offset="0" stop-color="#ffffff"/>
          <stop offset=".35" stop-color="#eef5d9"/>
          <stop offset=".6" stop-color="#a9d35f"/>
          <stop offset="1" stop-color="#2a8a37"/>
        </linearGradient>
        <linearGradient id="care-photo" x1="0" y1="0" x2="1" y2="1">
          <stop offset="0" stop-color="#e9d9cf"/>
          <stop offset=".45" stop-color="#c99a86"/>
          <stop offset="1" stop-color="#a9cfe0"/>
        </linearGradient>
        <linearGradient id="photo-fade" x1="0" y1="0" x2="1" y2="0">
          <stop offset="0" stop-color="#ffffff" stop-opacity="1"/>
          <stop offset=".25" stop-color="#ffffff" stop-opacity="0"/>
        </linearGradient>
        <linearGradient id="photo-fade-bottom" x1="0" y1="0" x2="0" y2="1">
          <stop offset=".7" stop-color="#ffffff" stop-opacity="0"/>
          <stop offset="1" stop-color="#ffffff" stop-opacity="1"/>
        </linearGradient>
        <linearGradient id="house-photo" x1="0" y1="0" x2="1" y2="1">
          <stop offset="0" stop-color="#f3e1d4"/>
          <stop offset=".55" stop-color="#e2b79f"/>
          <stop offset="1" stop-color="#7dbb45"/>
        </linearGradient>
      </defs>

      <rect x="0" y="0" width="320" height="679" fill="url(#promise-bg)"/>
      <rect x="320" y="0" width="320" height="679" fill="url(#bokeh-bg)" role="img" aria-label="Soft green bokeh background of blurred foliage"/>
      <rect x="640" y="0" width="320" height="679" fill="#ffffff"/>

      <path d="M0 0 H640 V40 C560 70 430 112 300 108 C190 104 90 92 0 78 Z" fill="var(--lime)"/>
      <path d="M0 78 C90 92 190 104 300 108 C430 112 560 70 640 40 V58 C560 90 430 130 300 126 C190 122 90 110 0 98 Z" fill="var(--salmon)"/>
      <path d="M320 160 C420 150 540 130 640 90" fill="none" stroke="var(--lime-soft)" stroke-width="6"/>

      <rect x="70" y="130" width="230" height="150" rx="6" fill="url(#house-photo)" role="img" aria-label="Photo of cupped hands holding a small green paper house"/>

      <rect x="640" y="0" width="320" height="430" fill="url(#care-photo)" role="img" aria-label="Photo of a caregiver's hands gently holding an elderly client's hands"/>
      <rect x="640" y="0" width="320" height="430" fill="url(#photo-fade)"/>
      <rect x="640" y="0" width="320" height="430" fill="url(#photo-fade-bottom)"/>

      <path d="M640 470 C670 600 800 640 960 628 V679 H640 Z" fill="var(--salmon)"/>
      <path d="M640 470 C672 585 800 622 960 610 V628 C800 640 670 600 640 470 Z" fill="var(--leaf)"/>
      <path d="M650 500 C690 600 810 630 960 620" fill="none" stroke="var(--lime-soft)" stroke-width="3"/>
      <path d="M640 0 H960 V12 C860 40 740 30 640 60 Z" fill="var(--lime)" opacity=".9"/>
    </svg>

    <section class="panel panel--promise">
      <h2 class="promise-title"><span class="lead">The</span><span class="lead">Thornbury Homecare</span><span class="main">Promise</span></h2>
      <div class="promise-copy">
        <p><strong>Thornbury Homecare</strong> is a home health agency located in Fairhaven, Hawaii.</p>
        <p>We provide in-home services ranging from light housekeeping to skilled nursing services. We focus on providing the highest level of quality home care while offering the best value to our clients.</p>
        <p>The Thornbury Way is special. It is compassionate, professional, dependable, flexible and is built on the strongest foundation. Everything we do is focused on meeting the individual needs of our clients.</p>
      </div>
    </section>

    <section class="panel panel--contact">
      <address class="contact-block">
        <p class="contact-name">Thornbury Homecare</p>
        <p class="contact-line">480 Lantern Ridge Ave, Suite 210, Fairhaven, HI 96700</p>
        <p class="contact-line">Phone: 808-555-0142 | Fax: 808-555-0148</p>
        <p class="contact-line">Email: info@thornburycare-example.com</p>
      </address>
    </section>

    <section class="panel panel--cover">
      <div class="brand-lockup">
        <span class="brand-mark"></span>
        <span class="brand-name">Thornbury Homecare</span>
      </div>
      <p class="brand-tagline">Someone you can depend on…<br>Without question.</p>
    </section>
  </div>
</div>
</body>
</html>
```